Business card design/logo/website name

I am a business coach. My business name is DKA (Dunmore Kesby & Associates, Inc.) I want to use this card just for coaching. I do two kinds: Personal Image coach and Executive business coach
1. I work with people to become a polished global professional.
"Become a confident, savvy professional building relationships tactfully and appropriately while clearly representing your own company’s message and image.
Learn the nuances… Master the skills… Use the business etiquette techniques and protocols that allow you to seamlessly and confidently conduct business in a global business environment.
Have the comfort of knowing what to expect, what to do and how to easily build long and short-term relationships that give you the winning edge and increased company profits."
2. Leadership Coaching
For increasing the team’s productivity by building stronger relationships. Build strong compelling vision and write and share their Personal Leadership Philosophy, a roadmap that is concise and commanding and gives the team a clear vision of the leader's expectations.

DKA should be the logo. (Downplay the Dunmore Kesby and Associates, Inc.)

Want:
Executive Coach
Consultant

Reason: I am traveling and connections are often broken.

Target Market(s)

Executives, business people

Industry/Entity Type

Building

Font styles to use
Sans Serif
Script

Colors
0255a3
3176b5
85acd3
ec2027

Requirements
Must have
• DKA as the logo,(no preference on how you treat DKA) with Dunmore Kesby & Associates. Inc. downplayed.
On the card:
Rosalind Kesby CEO
Executive Coach
Consultant
NVQ 4(c)
Coaching - Training - Strategic Planning

```html
<!DOCTYPE html>
<html lang="en">
<head>
<meta charset="utf-8">
<title>DKA Business Card</title>
<link rel="stylesheet" href="https://fonts.googleapis.com/css2?family=Oswald:wght@400;500&family=Arimo:wght@400&display=swap">
<style>
  :root {
    --blue-deep: #0255a3;
    --blue-mid: #3176b5;
    --blue-light: #85acd3;
    --red: #ec2027;
    --white: #ffffff;
    --backdrop: #e9ecef;
    --logo-violet: #4a4fb0;
  }
  * { box-sizing: border-box; margin: 0; padding: 0; }
  html, body { width: 1200px; height: 900px; overflow: hidden; }
  body {
    background: var(--backdrop);
    position: relative;
    font-family: "Oswald", sans-serif;
  }
  .card {
    position: absolute;
    left: 290px;
    width: 620px;
    height: 354px;
    background: var(--white);
    overflow: hidden;
    box-shadow: 0 6px 18px rgba(0,0,0,0.18);
  }
  .card--front { top: 70px; }
  .card--back { top: 476px; }

  /* Front */
  .front-band {
    position: absolute;
    left: 0; right: 0; bottom: 0;
    height: 88px;
    background: linear-gradient(180deg, var(--blue-mid), var(--blue-deep));
    display: flex;
    justify-content: center;
    align-items: center;
    gap: 18px;
    padding: 0 30px;
  }
  .service {
    color: var(--white);
    font-size: 21px;
    font-weight: 500;
    letter-spacing: 0.5px;
    text-transform: uppercase;
  }
  .service-divider {
    color: var(--blue-light);
    font-size: 21px;
    font-weight: 500;
  }
  .brand {
    position: absolute;
    top: 78px;
    left: 0; right: 0;
    text-align: center;
  }
  .brand-mark {
    font-family: "Arimo", sans-serif;
    font-size: 96px;
    line-height: 1;
    color: var(--logo-violet);
    letter-spacing: 4px;
  }
  .brand-name {
    font-family: "Arimo", sans-serif;
    font-size: 15px;
    color: var(--logo-violet);
    margin-top: 8px;
  }

  /* Back */
  .back-band {
    position: absolute;
    left: 0; right: 0; bottom: 0;
    height: 120px;
    background: linear-gradient(180deg, var(--blue-mid), var(--blue-deep));
  }
  .name-panel {
    position: absolute;
    left: 0; top: 0;
    width: 330px;
    height: 290px;
    background: var(--white);
  }
  .accent-bar {
    position: absolute;
    left: 236px; top: 0;
    width: 30px; height: 140px;
    background: var(--blue-mid);
  }
  .identity {
    position: absolute;
    left: 40px; top: 156px;
    text-align: right;
    width: 270px;
  }
  .person-name {
    color: var(--blue-deep);
    font-size: 26px;
    font-weight: 500;
    text-transform: uppercase;
    line-height: 1.15;
    margin-bottom: 2px;
  }
  .person-role {
    color: var(--red);
    font-size: 15px;
    font-weight: 500;
    text-transform: uppercase;
    line-height: 1.3;
  }
  .contact-list {
    position: absolute;
    left: 360px; top: 56px;
    list-style: none;
  }
  .contact-item {
    display: flex;
    align-items: flex-start;
    gap: 10px;
    margin-bottom: 8px;
    color: var(--blue-mid);
    font-size: 15px;
    text-transform: uppercase;
    line-height: 1.3;
  }
  .contact-icon {
    flex: none;
    width: 22px; height: 22px;
    background: var(--red);
    border: 2px solid var(--blue-light);
    display: flex; align-items: center; justify-content: center;
  }
  .contact-icon svg { width: 13px; height: 13px; }
</style>
</head>
<body>

<section class="card card--front" aria-label="Card front">
  <div class="brand">
    <div class="brand-mark">DKA</div>
    <div class="brand-name">Dunmore Kesby &amp; Associates, Inc.</div>
  </div>
  <div class="front-band">
    <span class="service">Coaching</span>
    <span class="service-divider">-</span>
    <span class="service">Training</span>
    <span class="service-divider">-</span>
    <span class="service">Strategic Planning</span>
  </div>
</section>

<section class="card card--back" aria-label="Card back">
  <div class="back-band"></div>
  <div class="name-panel"></div>
  <div class="accent-bar"></div>
  <div class="identity">
    <div class="person-name">Rosalind L. Kesby</div>
    <div class="person-role">CEO</div>
    <div class="person-role">Executive Coach</div>
    <div class="person-role">Consultant</div>
    <div class="person-role">NVQ 4(c)</div>
  </div>
  <ul class="contact-list">
    <li class="contact-item">
      <span class="contact-icon"><svg viewBox="0 0 16 16"><path fill="#fff" d="M3 1l3 3-1.5 2c1 2 3 4 5 5l2-1.5 3 3-2 2C7 14 2 9 1 3z"/></svg></span>
      <span>555-318-2764</span>
    </li>
    <li class="contact-item">
      <span class="contact-icon"><svg viewBox="0 0 16 16"><circle cx="8" cy="8" r="3" fill="none" stroke="#fff" stroke-width="2"/><path d="M11 5v4a2 2 0 0 0 4 0V8a7 7 0 1 0-3 5.7" fill="none" stroke="#fff" stroke-width="1.6"/></svg></span>
      <span>rkesby@dunmorekesby.com</span>
    </li>
    <li class="contact-item">
      <span class="contact-icon"><svg viewBox="0 0 16 16" fill="none" stroke="#fff" stroke-width="1.4"><circle cx="8" cy="8" r="6.5"/><ellipse cx="8" cy="8" rx="3" ry="6.5"/><path d="M1.5 8h13M3 4.5h10M3 11.5h10"/></svg></span>
      <span>www.dunmorekesby.com</span>
    </li>
    <li class="contact-item">
      <span class="contact-icon"><svg viewBox="0 0 16 16"><path fill="#fff" d="M8 1l7 4H1zM2 6h12v1H2zM3 8h2v5H3zM7 8h2v5H7zM11 8h2v5h-2zM1 14h14v1.5H1z"/></svg></span>
      <span>2940 Harbor Pine Road,<br>Fairview, OR 97024</span>
    </li>
  </ul>
</section>

</body>
</html>
```